Company or website name
- www.pmrtechworks.net Harbor Value Systems DBA PMRTechworks
- Links to the website
- www.pmrtechworks.net
- Describe your company and organization and target audience
- We are targeting business customers- small to medium size. The ideal client will have the need fo PC's laptops servers wiring Managed services security cameras etc.
- The design should have the following
- CLEAN design, no humor with a call to action toward our product and services.  Zantrix PC laptop and server products Video surveillance systems Point of sale systems Ledgerwise Assistance Warranty service Managed services Data protection and backup Network security Wiring
- Other Facts

```html
<!DOCTYPE html>
<html lang="en">
<head>
<meta charset="utf-8">
<title>PMRTechworks Trifold Brochure</title>
<link href="https://fonts.googleapis.com/css2?family=Open+Sans:ital,wght@0,400;0,600;0,700;0,800;1,400;1,600;1,700&display=swap" rel="stylesheet">
<style>
:root{
  --navy:#1c2a5c;
  --navy-deep:#141f47;
  --blue:#3b86cf;
  --blue-light:#5aa3e0;
  --ink:#2b2f3a;
  --muted:#6b7180;
  --soft:#c7cde0;
  --paper:#ffffff;
  --paper-grey:#f1f2f4;
  --backdrop:#e6e8eb;
}
*{box-sizing:border-box;margin:0;padding:0}
html,body{width:901px;height:1200px;overflow:hidden}
body{background:var(--backdrop);font-family:"Open Sans",Arial,sans-serif;color:var(--ink);position:relative}
.spread{position:absolute;left:30px;width:840px;height:500px;display:flex;box-shadow:0 6px 18px rgba(0,0,0,.12)}
.spread--inside{top:40px}
.spread--outside{top:640px}
.panel{position:relative;width:280px;height:500px;background:var(--paper);overflow:hidden}
.photo{position:absolute;left:0;width:100%}
.band{position:absolute;left:0;width:100%;background:var(--navy)}
.headline{position:absolute;left:18px;right:18px;color:var(--navy);font-weight:700;font-style:italic;font-size:15px;line-height:1.2}
.body-copy{position:absolute;left:18px;right:18px;font-size:7.5px;line-height:1.5;color:var(--muted)}
.body-copy p+p{margin-top:6px}
.partner{position:absolute;font-weight:700;font-size:11px;color:var(--navy)}

/* inside left */
.inside-left .photo{top:0;height:215px;background:linear-gradient(160deg,#f4f5f7 0%,#dfe2e6 60%,#c9cdd3 100%)}
.inside-left .band{top:195px;height:40px;clip-path:polygon(0 60%,100% 0,100% 35%,0 100%)}
.inside-left .headline{top:240px}
.inside-left .body-copy{top:285px}
.inside-left .footer{position:absolute;left:0;bottom:0;width:100%;height:56px;background:var(--paper-grey);clip-path:polygon(0 20%,100% 0,100% 100%,0 100%)}
.badge{position:absolute;left:18px;bottom:14px;width:72px;height:26px;background:var(--blue);border-radius:2px}
.inside-left .partner{right:22px;bottom:20px}

/* inside middle */
.inside-middle .photo{top:0;height:175px;background:linear-gradient(180deg,#eef0f2 0%,#d4d7dc 100%)}
.inside-middle .band{top:150px;height:255px;clip-path:polygon(0 12%,100% 0,100% 88%,0 100%)}
.services{position:absolute;top:192px;left:16px;right:0;list-style:none}
.services li{display:flex;align-items:center;height:27px;margin-bottom:5px;background:var(--blue);color:#fff;font-size:7.5px;font-weight:700;letter-spacing:.3px;text-transform:uppercase}
.services .icon{width:26px;height:27px;background:var(--blue-light);display:flex;align-items:center;justify-content:center;margin-right:10px}
.inside-middle .partner--a{left:22px;bottom:28px}
.inside-middle .partner--b{right:22px;bottom:28px}

/* inside right */
.inside-right .photo{top:0;height:130px;background:linear-gradient(200deg,#f6f6f7 0%,#e2e4e7 100%)}
.inside-right .band{top:110px;height:44px;clip-path:polygon(0 100%,100% 0,100% 45%,0 100%)}
.inside-right .headline{top:150px}
.inside-right .body-copy{top:192px}
.brand{position:absolute;display:flex;align-items:center;gap:6px;font-weight:800;color:var(--navy)}
.inside-right .brand{left:70px;top:318px;font-size:18px}
.brand .square{width:12px;height:12px;background:var(--blue)}
.inside-right .partner--a{left:22px;bottom:24px}
.inside-right .partner--b{right:22px;bottom:40px}

/* outside left */
.outside-left .photo{top:0;height:175px;background:radial-gradient(circle at 45% 50%,#d7dde6 0%,#a9b5c4 45%,#5d6a7d 100%)}
.outside-left .band{top:160px;height:40px;clip-path:polygon(0 70%,100% 0,100% 40%,0 100%)}
.outside-left .headline{top:205px;font-size:14px}
.outside-left .body-copy{top:270px}
.check-list{position:absolute;top:335px;left:18px;right:18px;list-style:none;font-size:7px;color:var(--muted)}
.check-list li{position:relative;padding-left:12px;margin-bottom:7px}
.check-list li::before{content:"";position:absolute;left:0;top:2px;width:5px;height:5px;border-radius:50%;background:var(--blue)}
.check-list .lead{padding-left:0;font-weight:600;color:var(--ink)}
.check-list .lead::before{display:none}

/* outside middle */
.outside-middle{background:var(--navy);color:#fff}
.outside-middle .top{position:absolute;top:0;left:0;width:100%;height:40px;background:var(--navy-deep)}
.outside-middle h2{position:absolute;top:16px;left:18px;right:14px;font-size:14px;font-weight:700;font-style:italic;line-height:1.2}
.outside-middle .intro{position:absolute;top:42px;left:18px;right:14px;font-size:7.5px;line-height:1.45}
.perks{position:absolute;top:84px;left:18px;right:14px;list-style:none}
.perks li{position:relative;padding-left:18px;margin-bottom:11px;line-height:1.3}
.perks li::before{content:"";position:absolute;left:0;top:2px;width:8px;height:8px;border-radius:50%;background:#fff}
.perks strong{display:block;font-size:8px}
.perks span{display:block;margin-top:2px;font-size:6.5px;color:var(--soft)}
.contact{position:absolute;top:262px;left:18px;right:14px}
.contact h3{font-size:10px;font-style:italic;font-weight:700;margin-bottom:9px}
.contact-row{display:flex;gap:10px;margin-bottom:10px;line-height:1.3}
.contact-row svg{flex:none;margin-top:1px}
.contact-row b{display:block;font-size:7.5px}
.contact-row span{display:block;margin-top:2px;font-size:6.5px;color:var(--soft)}
.outside-middle .callout{position:absolute;left:0;bottom:0;width:100%;height:78px;background:var(--blue);clip-path:polygon(0 30%,100% 0,100% 100%,0 100%);display:flex;align-items:flex-end;justify-content:center;padding-bottom:18px;text-align:center;font-style:italic;font-weight:600;font-size:12px;line-height:1.2}

/* outside right (cover) */
.outside-right .brand{left:90px;top:40px;font-size:26px}
.outside-right .brand .square{width:16px;height:16px}
.tagline{position:absolute;top:100px;left:0;width:100%;text-align:center;color:var(--navy)}
.tagline small{display:block;font-size:13px;letter-spacing:1px}
.tagline strong{display:block;font-size:21px;font-weight:800;letter-spacing:.5px}
.outside-right .photo{top:160px;height:270px;background:linear-gradient(150deg,#e9ebee 0%,#c8ccd2 50%,#8e7b84 100%)}
.outside-right .footer{position:absolute;left:0;bottom:0;width:100%;height:90px;background:var(--navy);clip-path:polygon(0 25%,100% 0,100% 100%,0 100%);color:#fff;text-align:right;padding:34px 20px 0 0}
.outside-right .footer strong{display:block;font-size:20px;font-weight:700;letter-spacing:1px;line-height:1.2}
.outside-right .footer span{font-size:10px}
</style>
</head>
<body>

<section class="spread spread--inside" aria-label="Brochure inside">
  <article class="panel inside-left">
    <div class="photo" role="img" aria-label="Photo of an office desk with a notebook, phone and mouse"></div>
    <div class="band"></div>
    <h2 class="headline">We take care of technology so you can focus on your business!</h2>
    <div class="body-copy">
      <p>Every moment lost to technology trouble is a missed opportunity to move your business forward. Don't take a chance when it comes to your company and leave the IT to the professionals.</p>
      <p>Our company proudly participates in service and sales programs with leading makers. These programs ensure that our personnel and engineers have a good understanding and in-depth knowledge of the various computer, printer and software product lines.</p>
      <p>Our Service Engineers are trained and certified by each manufacturer, ensuring accurate analysis and faster return to service for our customers. We inventory a variety of spare parts for the repair of many computers, laptops, printers, faxes, plotters and multifunction units.</p>
    </div>
    <div class="footer"></div>
    <div class="badge"></div>
    <div class="partner">Lexora</div>
  </article>

  <article class="panel inside-middle">
    <div class="photo" role="img" aria-label="Photo of hands typing on a laptop beside a coffee cup"></div>
    <div class="band"></div>
    <ul class="services">
      <li><span class="icon"><svg width="12" height="10" viewBox="0 0 12 10"><rect x="1" y="1" width="10" height="6" fill="none" stroke="#fff"/><rect x="3" y="8" width="6" height="1" fill="#fff"/></svg></span>Zantrix PC laptop and server products</li>
      <li><span class="icon"><svg width="12" height="10" viewBox="0 0 12 10"><rect x="1" y="2" width="7" height="6" fill="#fff"/><polygon points="8,5 11,2 11,8" fill="#fff"/></svg></span>Video surveillance systems</li>
      <li><span class="icon"><svg width="12" height="10" viewBox="0 0 12 10"><rect x="1" y="1" width="10" height="8" fill="none" stroke="#fff"/><rect x="3" y="3" width="6" height="2" fill="#fff"/></svg></span>Point of sale systems</li>
      <li><span class="icon"><svg width="12" height="10" viewBox="0 0 12 10"><rect x="2" y="1" width="8" height="8" fill="none" stroke="#fff"/><line x1="4" y1="4" x2="8" y2="4" stroke="#fff"/><line x1="4" y1="6" x2="8" y2="6" stroke="#fff"/></svg></span>Ledgerwise assistance</li>
      <li><span class="icon"><svg width="12" height="10" viewBox="0 0 12 10"><circle cx="6" cy="5" r="4" fill="none" stroke="#fff"/><polyline points="4,5 5.5,6.5 8,3.5" fill="none" stroke="#fff"/></svg></span>Warranty service</li>
      <li><span class="icon"><svg width="12" height="10" viewBox="0 0 12 10"><rect x="1" y="3" width="10" height="6" fill="none" stroke="#fff"/><rect x="4" y="1" width="4" height="2" fill="none" stroke="#fff"/></svg></span>Managed services</li>
    </ul>
    <div class="partner partner--a">Stonemark</div>
    <div class="partner partner--b">Ledgerwise</div>
  </article>

  <article class="panel inside-right">
    <div class="photo" role="img" aria-label="Photo of a white desk with a coffee cup"></div>
    <div class="band"></div>
    <h2 class="headline">Stop waiting for your technology to break!</h2>
    <div class="body-copy">
      <p>When something goes wrong with your IT, everything grinds to a halt. With a standard break-fix service contract, you have to wait for something to break before your provider will fix it. That expensive waiting game means hours of downtime. But what if you could keep your IT from breaking in the first place?</p>
    </div>
    <div class="brand"><span class="square"></span>PMRTechworks</div>
    <div class="partner partner--a">Wardline</div>
    <div class="partner partner--b">Zantrix</div>
  </article>
</section>

<section class="spread spread--outside" aria-label="Brochure outside">
  <article class="panel outside-left">
    <div class="photo" role="img" aria-label="Photo of a dome security camera"></div>
    <div class="band"></div>
    <h2 class="headline">Surveillance Systems don't have to be complicated or expensive but they should be expandable!</h2>
    <div class="body-copy">
      <p>Many security companies don't understand your technology, and budget cuts leave you stuck. We design systems that grow with your business and work with the network you already rely on every day.</p>
    </div>
    <ul class="check-list">
      <li class="lead">Our surveillance system services include:</li>
      <li>Camera systems for every size of site</li>
      <li>Remote viewing from phone and laptop</li>
      <li>Video storage built to fit your needs</li>
      <li>Clear plans, honest pricing, fast install</li>
      <li>Support from a local team you can trust</li>
    </ul>
  </article>

  <article class="panel outside-middle">
    <div class="top"></div>
    <h2>Are you tired of IT issues?</h2>
    <p class="intro">Talk to the team at Harbor Value Systems and let us show you how we can help you. With managed services from PMRTechworks, you can expect:</p>
    <ul class="perks">
      <li><strong>Peace of mind</strong><span>Your systems are monitored 24/7</span></li>
      <li><strong>Less downtime</strong><span>We identify and fix issues before they cause problems</span></li>
      <li><strong>Fewer disruptions</strong><span>We provide most services remotely or overnight</span></li>
      <li><strong>Predictable budgeting</strong><span>All-inclusive, flat-rate IT services that include hardware and software</span></li>
    </ul>
    <div class="contact">
      <h3>Contact informations:</h3>
      <div class="contact-row">
        <svg width="10" height="12" viewBox="0 0 10 12"><path d="M5 11 C1 6 1 5 1 4 A4 4 0 0 1 9 4 C9 5 9 6 5 11Z" fill="#fff"/></svg>
        <div><b>Address:</b><span>410 Harbor Street, Eastport NY 14000</span></div>
      </div>
      <div class="contact-row">
        <svg width="10" height="12" viewBox="0 0 10 12"><rect x="2" y="1" width="6" height="10" rx="1" fill="#fff"/></svg>
        <div><b>Phone number:</b><span>555-014-2290</span></div>
      </div>
      <div class="contact-row">
        <svg width="10" height="12" viewBox="0 0 10 12"><rect x="1" y="4" width="8" height="6" fill="#fff"/><rect x="3" y="1" width="4" height="3" fill="#fff"/></svg>
        <div><b>Fax:</b><span>555-014-2291</span></div>
      </div>
      <div class="contact-row">
        <svg width="10" height="12" viewBox="0 0 10 12"><circle cx="5" cy="6" r="4" fill="none" stroke="#fff"/><line x1="1" y1="6" x2="9" y2="6" stroke="#fff"/></svg>
        <div><b>Web address:</b><span>www.pmrtechworks.net</span></div>
      </div>
    </div>
    <div class="callout">PMR helps you work smarter,<br>not harder!</div>
  </article>

  <article class="panel outside-right">
    <div class="brand"><span class="square"></span>PMR</div>
    <div class="tagline"><small>we make your</small><strong>TECHNOLOGY WORK</strong></div>
    <div class="photo" role="img" aria-label="Photo of a laptop on a bright office desk"></div>
    <div class="footer"><strong>555-014-2290</strong><span>www.pmrtechworks.net</span></div>
  </article>
</section>

</body>
</html>
```